Flyer-Design - Coaching & Supervision für freib. Dipl.-Psychologin - BITTE KEINE WEITEREN DESINGS
Zielgruppe
--------- An alle, die überlegen mitzumachen - ich habe gerade als ungefähren Zeitplan, dass ich mich bis Donnerstag Abend (27.01.) entscheide, damit dann am Freitag (+evtl. Wochenende) noch Zeit für das Feintuning ist. -------------------
Ich bin Diplom-Psychologin und arbeite unter anderem freiberuflich als Coach und Supervisorin. Für diese Arbeit brauche ich einen Flyer. Ich habe bereits ein Konzept mit den Inhalten erstellt und brauche dafür nun ein professionelles Layout.
Aufgabenstellung
Anbei finden Sie das Konzept 1x als ppt (inklusive ausprobierter Alternativen zu den Fotos) und 1x als pdf.
Der Flyer hat als zentrales Thema „sich verändern / sich auf den Weg machen“ sowie die Analogie, dass ein gutes Coachinggespräch wie eine Bergtour ist.
Ich habe viel Vorarbeit gemacht (Inhalte stehen, Fotos sind recherchiert…) – sehr gerne können Sie sich kreativ ausleben und was völlig Neues / alles anders machen, es wäre aber auch ok, wenn das bereits Erarbeitete einfach graphisch aufgepimpt und professionalisiert wird.
Mein Wunsch: Ich weiß, dass der Flyer sehr voll ist. Aber ich möchte bewusst relativ viel Info dort unterbringen. Deshalb wäre es gut, wenn die Grafik des Flyers eine gewisse Leichtigkeit beinhaltet, die den vielen Text eher kaschiert. Also nicht zu verschnörkelt, sondern eher schlicht, hell und das Auge entlastend. Ich wünsche mir warme Farbtöne, die einladen und nicht zu kühl-modern wirken.
Logo:
Das Logo habe ich hier auf der Seite gestaltmarkt.de entwickeln lassen und habe alle Rechte daran. Es kann bei Bedarf auch angepasst werden.
Aktuell ist das Logo in grün, da ich dadurch den Naturbezug meiner Metapher mit aufgreife und weil die gerade entstehende Homepage, aktuell auch grün als Grundfarbe hat. Allerdings werde ich die Homepage auch noch professional überarbeiten lassen. Anbei einen Screenshot wie die Startseite der Homepage im Moment so ca. aussieht.
Bilder:
Die Fotos von mir hat ein Fotograf gemacht und ich darf sie verwenden.
Die Landschaftsbilder habe ich kostenlos und lizenzfrei von Lumora Bild ( https://bild.lumora-fotos.de/de/frei ) und von Fotelix ( https://fotelix-bilder.de/de/ ) heruntergeladen.
Falls Sie andere Bilder besser fänden und diese vorschlagen wollen, dann finden Sie weitere Details zu meinen Wünschen an die Bilder im Dokument „SelmK_AusschreibungDetails“
Die Landkarte ist ein Screenshot von KartoWeltNetz. Dort steht i..

```html
<!DOCTYPE html>
<html lang="de">
<head>
<meta charset="utf-8">
<title>Coaching &amp; Supervision – Flyer</title>
<link rel="stylesheet" href="https://fonts.googleapis.com/css2?family=Alegreya:ital,wght@0,400;0,500;1,400;1,500&family=Open+Sans:wght@400;600&display=swap">
<style>
:root{
  --sky:#c9d6e0;
  --meadow:#8b8a48;
  --steel:#6b97b8;
  --peach:#fbe6cf;
  --peach-line:#eab36a;
  --peach-head:#e9a549;
  --sage:#94a874;
  --sage-light:#b8c18b;
  --stone:#ebebdf;
  --ice:#e3f0f5;
  --ice-head:#4a87b0;
  --ice-line:#4a87b0;
  --amber:#efb04f;
  --leaf:#4e7a2a;
  --ink:#2f2f2f;
  --white:#ffffff;
}
*{box-sizing:border-box;margin:0;padding:0}
html,body{width:1200px;height:854px;overflow:hidden;background:var(--white)}
body{position:relative;font-family:"Open Sans",Arial,sans-serif;color:var(--ink)}
.block{position:absolute}
.heading{font-family:"Alegreya",Georgia,serif;font-weight:400;line-height:1.1}
.body-text{font-size:12.6px;line-height:1.35}

.hero-photo{left:0;top:0;width:805px;height:473px;
  background:linear-gradient(180deg,#b7c9d8 0%,#dde4e6 38%,#c8c3a0 58%,#8b8a48 75%,#6a6a36 100%)}
.sprout-photo{left:937px;top:374px;width:263px;height:265px;
  background:radial-gradient(circle at 78% 45%,#e6b820 0%,#9aa83a 14%,#4d6a22 40%,#2a3418 75%,#1c1a14 100%)}

.intro{left:427px;top:0;width:354px;height:187px;background:var(--steel);color:var(--white);padding:37px 20px 0 21px}
.intro .heading{font-size:21px;margin-bottom:8px}
.intro .body-text{font-size:12.6px;line-height:1.36}

.stance{left:830px;top:24px;width:345px;height:329px;background:var(--peach);padding:14px 20px 0 17px}
.stance .heading{color:var(--peach-head);font-size:19px}
.stance-grid{display:grid;grid-template-columns:152px 150px;row-gap:12px;margin:16px 0 0 12px}
.stance-item{border-left:2px solid var(--peach-line);padding-left:12px;height:41px;display:flex;align-items:center;font-weight:600;font-size:13.5px;line-height:1.2}
.stance .subhead{font-size:19px;margin:38px 0 16px 4px}
.stance .body-text{margin-left:4px}

.growth{left:805px;top:374px;width:132px;height:265px;background:var(--sage);color:var(--white);padding:26px 10px 0 25px;font-size:12.6px;line-height:1.15}
.growth li{list-style:none;width:81px;padding-bottom:12px}
.growth li + li{border-top:1.5px solid var(--white);padding-top:12px}

.metaphor{left:24px;top:393px;width:354px;height:251px;background:var(--stone);padding:16px 18px 0 21px}
.metaphor .heading{color:var(--leaf);font-style:italic;font-size:20.5px;line-height:1.2;margin-bottom:20px}
.metaphor .lead{font-family:"Alegreya",Georgia,serif;font-weight:500;font-size:14px;margin-bottom:4px}
.metaphor .body-text + .body-text{margin-top:16px}

.path{left:24px;top:665px;width:354px;height:164px;background:var(--sage-light);color:var(--white);padding:16px 18px 0 21px}
.path .heading{font-size:21px;margin-bottom:10px}
.path p{font-size:16px;line-height:1.25}

.topics{left:427px;top:493px;width:354px;height:336px;background:var(--ice);padding:18px 18px 0 21px}
.topics .heading{color:var(--ice-head);font-size:19px;margin-bottom:10px}
.topics .subhead{margin:54px 0 24px -2px}
.topic-grid{display:grid;grid-template-columns:156px 150px;row-gap:14px}
.topic-item{border-left:2px solid var(--ice-line);padding-left:13px;height:41px;display:flex;align-items:center;font-weight:600;font-size:13.5px;line-height:1.2}

.answer{left:830px;top:661px;width:345px;height:168px;background:var(--amber);color:var(--white);padding:16px 20px 0 21px}
.answer .heading{font-size:21px;line-height:1.02;margin-bottom:8px}
.answer p{font-size:16px;line-height:1.28}
</style>
</head>
<body>
  <div class="block hero-photo" role="img" aria-label="Zwei Wandernde mit Rucksäcken auf einer blühenden Bergwiese unter hellem Himmel"></div>

  <section class="block intro">
    <h2 class="heading">Was ist Coaching &amp; Supervision?</h2>
    <p class="body-text">Im Coaching und in der Supervision haben Sie die Möglichkeit, Ihr eigenes Handeln im beruflichen Kontext zu reflektieren. Mit Hilfe von strukturierten Gesprächen und ausgewählten Methoden begleite ich Sie dabei, in einem geschützten Rahmen eigene Lösungen zu entwickeln und umzusetzen.</p>
  </section>

  <section class="block stance">
    <h2 class="heading">Meine Grundhaltung:</h2>
    <div class="stance-grid">
      <div class="stance-item">systemisch</div>
      <div class="stance-item">lösungs- und<br>zielorientiert</div>
      <div class="stance-item">ressourcen-<br>orientiert</div>
      <div class="stance-item">wertschätzend</div>
    </div>
    <h3 class="heading subhead" style="color:var(--peach-head)">Ich habe keine „Beratungsschablonen“.</h3>
    <p class="body-text">Mir ist wichtig, mit welcher Arbeitsmethode Sie sich wohlfühlen. Deshalb passe ich die Methoden situativ Ihren Bedürfnissen an. Dazu bringe ich einen großen Methodenschatz mit. Besonders wichtig ist mir der Transfer in den Alltag.</p>
  </section>

  <ul class="block growth">
    <li>Ressourcen Stärken</li>
    <li>an Heraus-<br>forderungen wachsen</li>
    <li>das Leben gestalten</li>
    <li>sich (weiter) entwickeln</li>
  </ul>
  <div class="block sprout-photo" role="img" aria-label="Junge Pflanzentriebe und eine gelbe Blüte wachsen aus dunkler Erde"></div>

  <section class="block metaphor">
    <h2 class="heading">Ein gutes Coachinggespräch ist<br>wie eine gemeinsame Bergtour…</h2>
    <p class="lead">Sie bestimmen das Thema – Ihren Berg.</p>
    <p class="body-text">Sie bestimmen das Tempo. Sie entdecken Ihre eigenen Ressourcen während Sie sich Schritt für Schritt Ihrem Ziel nähern.</p>
    <p class="body-text">Gemeinsam erkunden wir, welche Wege es zu Ihrem Ziel gibt. Ich begleite Sie auf allen Etappen. Ich helfe Ihnen, sich unterwegs zu orientieren.</p>
  </section>

  <section class="block path">
    <h2 class="heading">Wir gehen den Weg:</h2>
    <p>mit Offenheit, mit Neugierde, mit einem Lachen, mit einem klaren Blick, mit Pausen, mit Ausdauer, mit Freude, mit Motivation, mit allen Sinnen und allen Emotionen.</p>
  </section>

  <section class="block topics">
    <h2 class="heading">Geht es nur um berufliche Themen?</h2>
    <p class="body-text">Jein. Private Themen können Kraftgeber und Krafträuber sein und sich auf berufliche Themen auswirken. Es geht oft um die Balance im Leben und deshalb ist es gut beides im Auge zu haben. Coaching ist aber keine Therapie.</p>
    <h3 class="heading subhead">Häufige Themenfelder:</h3>
    <div class="topic-grid">
      <div class="topic-item">Berufliche<br>Kompetenzen</div>
      <div class="topic-item">Persönlichen<br>Kompetenzen</div>
      <div class="topic-item">Teamwork</div>
      <div class="topic-item">Supervison</div>
    </div>
  </section>

  <section class="block answer">
    <h2 class="heading">Die Antwort auf Ihre Frage liegt schon in Ihnen…</h2>
    <p>… ich helfe Ihnen, sie zu sehen. Und manchmal helfe ich auch, sich erstmal über die Frage klar zu werden.</p>
  </section>
</body>
</html>
```